Brochure design for 3D ultrasound company

I am looking for a clean and modern and edgy brochure for my ultrasound company. We are a fairly new company specialize in 3D/4D ultrasounds.Our brochures will be placed in OB-GYN offices in high end areas around Los Angeles, so we need something that will stand out and capture a modern woman's attention. Our logo is currently in the process of being designed, so I don't have a picture to provide quite yet, however it will be our company name"Kite + Fern" written in a special font that looks like neon lights. I will attach a few images of what our logo will be like, and some initial content that can help provide the layout we would like for the brochure. please feel free to also take a look at our website. www.kitefernscans.example.

Target Market(s)

Upscale trendy women.

Colors
eea4c8
33a6d7
fee18a

Requirements
Should not have
• too many colors.

```html
<!DOCTYPE html>
<html lang="en">
<head>
<meta charset="utf-8">
<title>Kite + Fern — Services + Pricing</title>
<link href="https://fonts.googleapis.com/css2?family=Open+Sans:ital,wght@0,300;0,400;0,700;0,800;1,700;1,800&family=Oswald:wght@600&display=swap" rel="stylesheet">
<style>
  :root {
    --pink: #eea4c8;
    --pink-deep: #fb9ddc;
    --pink-soft: #fde7f3;
    --blue: #33a6d7;
    --sky: #12b5f7;
    --lilac: #c6a5e8;
    --violet: #b28ad8;
    --ink: #111111;
    --text: #222222;
    --white: #ffffff;
  }
  * { margin: 0; padding: 0; box-sizing: border-box; }
  html, body { width: 1200px; height: 927px; overflow: hidden; background: var(--white); }
  body { font-family: "Open Sans", sans-serif; color: var(--text); }
  .brochure { position: relative; width: 1200px; height: 927px; overflow: hidden; }

  /* Left panel */
  .pricing-panel {
    position: absolute; left: 0; top: 0; width: 743px; height: 927px;
    background: linear-gradient(90deg, #ffffff 0%, var(--pink-soft) 30%, #fcc0e2 65%, var(--pink-deep) 100%);
  }
  .panel-title {
    position: absolute; left: 66px; top: 44px;
    font-weight: 800; font-size: 45px; letter-spacing: 0.27em; color: var(--ink); white-space: nowrap;
  }
  .panel-intro {
    position: absolute; left: 90px; top: 118px; width: 516px;
    font-weight: 300; font-size: 26px; line-height: 34px; text-align: center; color: var(--ink);
  }
  .package-photo { position: absolute; left: 28px; width: 302px; height: 180px; }
  .photo-newborn { top: 256px; background: linear-gradient(135deg, #f4f4f4, #bdbdbd 60%, #e8e8e8); }
  .photo-bump { top: 448px; background: radial-gradient(ellipse at 50% 55%, #8a7a68, #4d4034 55%, #121212 100%); }
  .photo-couple { top: 639px; background: linear-gradient(90deg, #e8e8e8 0%, #9a9a9a 35%, #2a2a2a 70%, #f0f0f0 100%); }

  .price-tag {
    position: absolute; left: 330px; width: 110px; height: 38px;
    background: linear-gradient(90deg, var(--pink-deep) 70%, rgba(251,157,220,0) 100%);
    font-weight: 700; font-size: 21px; line-height: 38px; padding-left: 10px; color: var(--ink);
  }
  .package-details { position: absolute; left: 446px; width: 290px; font-size: 18px; line-height: 25px; font-weight: 300; color: var(--ink); }
  .package-details h3 { font-size: 18px; font-weight: 700; line-height: 25px; }
  .package-details li { list-style: none; }
  .package-details li::before { content: "• "; font-size: 12px; vertical-align: middle; }

  /* Right panel */
  .feature-photo {
    position: absolute; left: 743px; top: 0; width: 457px; height: 455px;
    background: linear-gradient(160deg, #b8464e 0%, #6b5560 30%, #3d4a62 55%, #a58a80 100%);
  }
  .feature-overlay {
    position: absolute; left: 914px; top: 58px; width: 286px; height: 397px;
    background: linear-gradient(180deg, rgba(200,150,230,0.8), rgba(190,140,220,0.75));
  }
  .feature-ribbon { position: absolute; left: 1020px; top: 38px; width: 24px; height: 417px; background: linear-gradient(180deg, #a9d6f2, #b6a6ef); opacity: 0.85; }
  .feature-kicker {
    position: absolute; right: 14px; top: 84px; text-align: right;
    font-weight: 800; font-size: 33px; line-height: 33px; letter-spacing: 0.27em; color: var(--white); margin-right: -9px;
  }
  .reveal-pill {
    position: absolute; left: 782px; top: 301px; width: 430px; height: 69px; border-radius: 35px 0 0 35px;
    background: linear-gradient(90deg, var(--sky) 0%, #6fb2f0 50%, var(--lilac) 100%);
    font-family: "Oswald", sans-serif; font-weight: 600; font-size: 39px; line-height: 69px;
    color: var(--white); padding-left: 56px; letter-spacing: 0.01em;
  }
  .reveal-price {
    position: absolute; left: 908px; top: 382px; width: 300px; height: 49px; border-radius: 25px 0 0 25px;
    background: linear-gradient(90deg, #2e3450 0%, #4a5a86 50%, var(--sky) 100%);
    font-weight: 800; font-size: 40px; line-height: 49px; letter-spacing: 0.08em; color: var(--white); padding-left: 38px;
  }
  .reveal-list { position: absolute; left: 776px; top: 478px; width: 410px; font-weight: 300; font-size: 21px; color: var(--ink); }
  .reveal-list ul { list-style: none; }
  .reveal-list li { position: relative; padding-left: 28px; }
  .reveal-list li::before { content: ""; position: absolute; left: 5px; top: 12px; width: 7px; height: 7px; border-radius: 50%; background: var(--ink); }
  .reveal-list .spaced li { line-height: 42px; }
  .reveal-list .tight li { line-height: 21px; padding-left: 33px; }
  .reveal-list .tight li::before { top: 8px; }
  .reveal-list p { line-height: 21px; margin-top: 5px; }

  .cta-band {
    position: absolute; left: 806px; top: 700px; width: 372px; height: 45px;
    background: linear-gradient(90deg, #9fd6fb 0%, #c9b3ef 55%, #f6a8dc 100%);
    clip-path: polygon(0 12%, 100% 0, 98% 100%, 2% 90%);
    font-weight: 800; font-style: italic; font-size: 17px; line-height: 45px; text-align: center; color: var(--ink);
  }
  .contact { position: absolute; left: 760px; width: 450px; text-align: center; font-size: 18px; color: var(--ink); }
  .contact-call { top: 762px; font-weight: 300; line-height: 25px; }
  .contact-web { top: 836px; font-weight: 300; line-height: 25px; }
  .contact strong { font-weight: 700; font-size: 19px; }
</style>
</head>
<body>
<main class="brochure">
  <section class="pricing-panel">
    <h1 class="panel-title">SERVICES+PRICING</h1>
    <p class="panel-intro">We are available for private in-home screenings, gender reveals, baby showers, or any other special occasion!</p>

    <div class="package-photo photo-newborn" role="img" aria-label="Black and white photo of a smiling newborn on a soft blanket"></div>
    <div class="price-tag" style="top:322px">$125.00</div>
    <div class="package-details" style="top:278px">
      <h3>PEEK -A -BOO:</h3>
      <ul><li>15 minute 2D session</li><li>3 black and white images</li><li>Listen to baby’s heartbeat</li><li>Confirm gender</li></ul>
    </div>

    <div class="package-photo photo-bump" role="img" aria-label="Photo of hands forming a heart shape on a pregnant belly"></div>
    <div class="price-tag" style="top:502px">$165.00</div>
    <div class="package-details" style="top:458px">
      <h3>HELLO , MOMMA:</h3>
      <ul><li>15 minute 3D/4D /HD live session</li><li>3 black and white images</li><li>2 color images</li><li>Listen to baby’s heartbeat</li><li>Confirm gender</li></ul>
    </div>

    <div class="package-photo photo-couple" role="img" aria-label="Black and white photo of a father resting his head on a pregnant belly"></div>
    <div class="price-tag" style="top:693px">$325.00</div>
    <div class="package-details" style="top:635px">
      <h3>V.I.B (VERY IMPORTANT BABY) :</h3>
      <ul><li>30 min 3D/4D/HD live session on our projector</li><li>10 color images</li><li>Email or USB with all images</li><li>Record and hear heartbeat</li><li>Confirm gender</li></ul>
    </div>
  </section>

  <section class="reveal-panel">
    <div class="feature-photo" role="img" aria-label="Photo of a pregnant belly wrapped with a ribbon bow, festive red background"></div>
    <div class="feature-overlay"></div>
    <div class="feature-ribbon"></div>
    <p class="feature-kicker">OUR MOST<br>POPULAR<br>PACKAGE</p>
    <h2 class="reveal-pill">THE BIG REVEAL!!</h2>
    <div class="reveal-price">$225</div>

    <div class="reveal-list">
      <ul class="spaced"><li>25 minute 3D/4D/HD live session</li><li>5 black and white pictures</li><li>5 color pictures</li></ul>
      <p>Email or USB flash drive with all images</p>
      <ul class="tight"><li>Record and hear heartbeat</li><li>Confirm gender</li></ul>
    </div>

    <p class="cta-band">Ready for your baby’s first photoshoot?</p>
    <p class="contact contact-call">Give us a call to schedule an appointment<br><strong>(555) 014-2280</strong></p>
    <p class="contact contact-web">or visit our website<br><strong>www.kitefernscans.example</strong></p>
  </section>
</main>
</body>
</html>
```